Facebook page as well as a business card and stationary design for a fitness instructor/personal trainer who is branching out as an independent worker delivering the gym experience (personal training or small group classes) to the home market. The trainer (RP or Rod Pellinger) is young, energetic, and results oriented.

Job Type
Facebook page and 2-sided business card
Task Outline
Create a Facebook presence (supported by a business card) for a train-you-at-home personal trainer
Task Description
Looking for a Graphic Designer/Web Designer to make a really modern/clean Facebook page that promotes Rod Pellinger ("RP") as at-your-home personal trainer. Rod's goal as a personal trainer is to motivate, inspire and educate all of his clients about the benefits of regular exercise, nourishing the body with nutritious foods, and living a healthy lifestyle while enjoying working out. He wants to encourage the convenience component of what he does by offering personal training sessions at a person's home or place of business. He trains both men and women, so the design of both the business card and the Facebook page should appeal to both genders and not come across as more feminine or more masculine. The Facebook page should include links to the Twitter, Instagram, and email accounts. It should also hold a placeholder link to his future web site called BougeAuLogis.

He holds several certifications and would like these mentioned on his Facebook page and perhaps on his business card -- either in text form or identifying them with the logos (which are attached).

Contact information for the business card will be supplied shortly. In the interim, the following can be used: Rod Pellinger Personal Trainer; Address: 287 Vauquelin, Dollard-des-Ormeaux, Quebec, J4K 7N2, Email: rpstrongdaily@mailbox.example; Phone: 514.302-4519; Facebook: RPStrongDaily; Twitter: RPStrongDaily; Website: BougeAuLogis.example

OTHER INFORMATION: This project is a Christmas present to the personal trainer who is a friend. He'll be making the final decisions on the designs for both components.
Updates

Target Market(s)

Both men and women who don't have the time for the gym and are looking for personal training at home or at their place of work.

Industry/Entity Type

Personal Trainer

Contact Information for Business Card

No photo. Clean lines and preference of blue colouring. contact information presented clearly. Card design must radiate the concept of fitness for life, living healthy and strong.

Font styles to use
Sans Serif

Colors
34a7d8
86cae6
85acd3
0355a3
0592ce
cee9f5
ceddec
86cfc6
cfeae6

```html
<!DOCTYPE html>
<html lang="fr">
<head>
<meta charset="utf-8">
<title>Bouge Au Logis — Couverture</title>
<link rel="stylesheet" href="https://fonts.googleapis.com/css2?family=Exo+2:wght@500&family=Open+Sans:wght@400&family=Playfair+Display:wght@700&display=swap">
<style>
  :root {
    --bg-deep: #02111f;
    --bg-mid: #06365a;
    --bg-glow: #1a7fb8;
    --band: rgba(0, 8, 16, 0.55);
    --band-line: rgba(134, 202, 230, 0.18);
    --text-white: #ffffff;
    --text-soft: #cee9f5;
    --text-band: #ceddec;
    --icon-top: #f4fbfe;
    --icon-bottom: #cee9f5;
    --icon-fade: rgba(134, 202, 230, 0.18);
  }
  * { margin: 0; padding: 0; box-sizing: border-box; }
  html, body {
    width: 1200px;
    height: 445px;
    overflow: hidden;
    background: var(--bg-deep);
  }
  .cover {
    position: relative;
    width: 1200px;
    height: 445px;
    overflow: hidden;
    background:
      radial-gradient(ellipse 540px 300px at 600px 230px, var(--bg-glow) 0%, var(--bg-mid) 45%, var(--bg-deep) 100%);
  }
  .brand-name {
    position: absolute;
    top: 76px;
    left: 0;
    width: 100%;
    text-align: center;
    font-family: "Playfair Display", serif;
    font-weight: 700;
    font-size: 35px;
    line-height: 44px;
    letter-spacing: 1px;
    color: var(--text-white);
  }
  .pillar-icons {
    position: absolute;
    left: 0;
    top: 196px;
    width: 100%;
    height: 66px;
  }
  .pillar-icon {
    position: absolute;
    top: 0;
    height: 66px;
    border-radius: 14px;
    background: linear-gradient(180deg, var(--icon-top), var(--icon-bottom));
    opacity: 0.92;
  }
  .pillar-icon--sport    { left: 336px; width: 72px; }
  .pillar-icon--food     { left: 456px; width: 72px; }
  .pillar-icon--weight   { left: 596px; width: 144px;
    background: linear-gradient(90deg, var(--icon-fade), var(--icon-bottom) 70%, var(--icon-top)); }
  .pillar-icon--wellness { left: 774px; width: 80px; }
  .pillars {
    position: absolute;
    top: 281px;
    left: 0;
    width: 100%;
    text-align: center;
    font-family: "Exo 2", sans-serif;
    font-weight: 500;
    font-size: 21px;
    line-height: 26px;
    letter-spacing: 0.5px;
    color: var(--text-white);
  }
  .pillars .divider { margin: 0 3px; color: var(--text-soft); }
  .tagline {
    position: absolute;
    top: 306px;
    left: 0;
    width: 100%;
    text-align: center;
    font-family: "Open Sans", sans-serif;
    font-size: 17px;
    line-height: 24px;
    color: var(--text-soft);
  }
  .contact-band {
    position: absolute;
    left: 0;
    top: 377px;
    width: 100%;
    height: 44px;
    background: var(--band);
    border-top: 1px solid var(--band-line);
    border-bottom: 1px solid var(--band-line);
    display: flex;
    align-items: center;
    justify-content: center;
    font-family: "Open Sans", sans-serif;
    font-size: 13px;
    color: var(--text-band);
    letter-spacing: 0.3px;
  }
</style>
</head>
<body>
  <main class="cover">
    <h1 class="brand-name">Bouge Au Logis</h1>

    <div class="pillar-icons">
      <div class="pillar-icon pillar-icon--sport" role="img" aria-label="Pictogramme d'un coureur en mouvement"></div>
      <div class="pillar-icon pillar-icon--food" role="img" aria-label="Pictogramme d'un haltère"></div>
      <div class="pillar-icon pillar-icon--weight" role="img" aria-label="Silhouettes successives montrant une perte de poids"></div>
      <div class="pillar-icon pillar-icon--wellness" role="img" aria-label="Silhouettes de deux personnes qui s'étirent"></div>
    </div>

    <p class="pillars">SPORT<span class="divider">|</span>ALIMENTATION<span class="divider">|</span>PERTE DE POIDS<span class="divider">|</span>BIEN-ÊTRE</p>
    <p class="tagline">Méthode et conseils pour perdre du poids</p>

    <footer class="contact-band">
      514.302-4519&nbsp;|&nbsp;287 Vauquelin, Dollard-des-Ormeaux, Quebec, J4K 7N2&nbsp;|&nbsp;WWW.BougeAuLogis.example
    </footer>
  </main>
</body>
</html>
```